Online-Marketing Material für Hundetraining
Zielgruppe
Hundetraining. Ich coache Hundehalter und unterstütze sie darin ihrem Hund Führung zu geben. Im Vordergrund steht die natürliche Kommunikation mit dem Hund - komplett ohne Leckerchen.
Aufgabenstellung
Ich brauche ein Design für eine Facebookwerbeanzeige. Der Titel meines Videokurses ist 'Gemeinsam stark im Alltag'. Inhaltlich geht es in dem Kurs darum, wie Hundehalter der akzeptierte Entscheidungsträger werden können, indem wir am Grundrespekt arbeiten und die eigene Führungskompetenzen ausbauen.

```html
<!DOCTYPE html>
<html lang="de">
<head>
<meta charset="utf-8">
<title>Gemeinsam stark im Alltag – Anzeige</title>
<link rel="stylesheet" href="https://fonts.googleapis.com/css2?family=Montserrat:wght@400;800&family=Open+Sans:wght@600;700&display=swap">
<style>
  :root {
    --stage: #7b797a;
    --teal-deep: #14958b;
    --teal-bright: #12b3a2;
    --teal-road: #3f8a87;
    --photo-sky: #d9e8e2;
    --photo-leaf: #5f8a55;
    --photo-trunk: #4a5a48;
    --photo-grass: #7fa35e;
    --photo-road: #55676b;
    --photo-road-dark: #3c4749;
    --photo-figure: #c9d2d6;
    --photo-denim: #26304a;
    --white: #ffffff;
    --cta: #e0901f;
  }
  * { box-sizing: border-box; margin: 0; padding: 0; }
  html, body {
    width: 1200px;
    height: 864px;
    overflow: hidden;
    background: var(--stage);
  }
  .ad {
    position: absolute;
    left: 131px;
    top: 150px;
    width: 939px;
    height: 565px;
    overflow: hidden;
    background: linear-gradient(115deg, var(--teal-road) 0%, var(--teal-deep) 50%, var(--teal-bright) 100%);
  }
  .ad__photo {
    position: absolute;
    left: 0;
    top: 0;
    width: 620px;
    height: 100%;
    background:
      radial-gradient(ellipse 120px 150px at 230px 250px, rgba(201,210,214,0.95) 0%, rgba(201,210,214,0.6) 55%, rgba(201,210,214,0) 100%),
      radial-gradient(ellipse 150px 140px at 220px 420px, rgba(38,48,74,0.9) 0%, rgba(38,48,74,0.5) 55%, rgba(38,48,74,0) 100%),
      linear-gradient(90deg, var(--photo-grass) 0%, rgba(127,163,94,0) 30%),
      linear-gradient(180deg, var(--photo-sky) 0%, var(--photo-leaf) 14%, var(--photo-trunk) 32%, var(--photo-leaf) 50%, var(--photo-road) 66%, var(--photo-road-dark) 100%);
    -webkit-mask-image: linear-gradient(90deg, #000 0%, #000 62%, rgba(0,0,0,0) 100%);
            mask-image: linear-gradient(90deg, #000 0%, #000 62%, rgba(0,0,0,0) 100%);
  }
  .ad__brand {
    position: absolute;
    left: 540px;
    width: 232px;
    top: 48px;
    display: flex;
    flex-direction: column;
    align-items: center;
    gap: 14px;
  }
  .ad__brand-dot {
    width: 70px;
    height: 70px;
    border-radius: 50%;
    background: var(--white);
  }
  .ad__brand-name {
    font-family: "Open Sans", sans-serif;
    font-weight: 700;
    font-size: 16px;
    letter-spacing: 0.3px;
    color: var(--white);
    text-transform: uppercase;
  }
  .ad__headline {
    position: absolute;
    left: 420px;
    width: 474px;
    top: 180px;
    text-align: center;
    font-family: "Montserrat", sans-serif;
    color: var(--white);
    font-size: 62px;
    line-height: 74px;
    text-transform: uppercase;
    letter-spacing: 0.5px;
  }
  .ad__headline strong { font-weight: 800; }
  .ad__headline .light { font-weight: 400; }
  .ad__cta {
    position: absolute;
    left: 524px;
    top: 439px;
    width: 254px;
    height: 49px;
    border-radius: 16px;
    background: var(--cta);
    box-shadow: 0 4px 10px rgba(0,0,0,0.18);
    display: flex;
    align-items: center;
    justify-content: center;
    font-family: "Open Sans", sans-serif;
    font-weight: 600;
    font-size: 20px;
    color: var(--white);
    text-transform: uppercase;
    text-decoration: none;
  }
</style>
</head>
<body>
  <section class="ad">
    <div class="ad__photo" role="img" aria-label="Foto: lachende Hundetrainerin kniet auf einem Alleeweg und hält einen fröhlichen braun-weißen Hütehund, Bäume und Wiese im Hintergrund"></div>
    <div class="ad__brand">
      <span class="ad__brand-dot"></span>
      <span class="ad__brand-name">Leinenwerk.de</span>
    </div>
    <h1 class="ad__headline">
      <strong>Gemeinsam</strong><br>
      <strong>Stark</strong> <span class="light">im</span><br>
      <span class="light">Alltag</span>
    </h1>
    <a class="ad__cta" href="#">Jetzt anmelden</a>
  </section>
</body>
</html>
```